Produktetikett für Mikronährstoffe
Wir sind sehr zufrieden und schätzen die schnelle Umsetzung von Änderungswünschen. Herzlichen Dank an Wilmaru
Zielgruppe
Herstellung und Vertrieb von Desinfektionsmitteln und jetz neu Mikronährstoffe. Und darum geht es. Wir möchten ein Etikett gestalten lassen das modern ist und trotzdem unsere Firmenfarben und unser Logo (evtl. stilisiert) enthält. Wahrscheinlich werden wir eine braune Flasche (ähnl. Apothekerflaschen) wählen.
Aufgabenstellung
Produktetikett für Mikronährstoffe (im Nahrungsergänzungsbereich) Die Ausführung der Flasche ist noch nicht bekannnt, jedoch schwebt uns eine braune oder dunkelgrüne Flasche vor. Auch gibt es noch keinen Namen für das Produkt.

```html
<!DOCTYPE html>
<html lang="de">
<head>
<meta charset="utf-8">
<title>Mikronährstoffkonzentrat – Etikett</title>
<link href="https://fonts.googleapis.com/css2?family=Montserrat:wght@400;500;700&family=Great+Vibes&display=swap" rel="stylesheet">
<style>
  :root {
    --brand-blue: #2aa3c6;
    --leaf-green: #9cc31f;
    --leaf-green-dark: #86ad12;
    --paper: #ffffff;
    --backdrop: #f1f1ef;
    --edge: #e2e6d8;
  }
  * { margin: 0; padding: 0; box-sizing: border-box; }
  html, body { width: 1200px; height: 1200px; overflow: hidden; }
  body {
    background: var(--backdrop);
    font-family: "Montserrat", sans-serif;
  }
  .label {
    position: absolute;
    left: 200px; top: 100px;
    width: 800px; height: 1000px;
    background: var(--paper);
    border: 2px solid var(--edge);
    overflow: hidden;
  }
  .brand {
    position: absolute;
    left: 0; right: 0; top: 70px;
    display: flex; align-items: center; justify-content: center; gap: 14px;
    color: var(--brand-blue);
    font-weight: 500;
    font-size: 52px;
    letter-spacing: 1px;
  }
  .brand-dot {
    width: 34px; height: 34px;
    border-radius: 50%;
    background: var(--leaf-green);
  }
  .tagline {
    position: absolute;
    left: 0; right: 0; top: 170px;
    text-align: center;
    font-family: "Great Vibes", cursive;
    font-weight: 400;
    font-size: 100px;
    line-height: 1.2;
    color: var(--brand-blue);
  }
  .tagline-swoosh { position: absolute; left: 150px; top: 300px; }
  .fruit-illustration {
    position: absolute;
    left: 70px; top: 360px;
    width: 560px; height: 240px;
    border-radius: 50% 50% 40% 40% / 60% 60% 40% 40%;
    background: radial-gradient(ellipse at 50% 55%, #f2b21c 0%, #c9d43a 45%, #9cc31f 75%, rgba(156,195,31,0) 100%);
  }
  .ingredient-badge {
    position: absolute;
    left: 560px; top: 520px;
    width: 150px; height: 150px;
    border-radius: 50%;
    background: var(--paper);
    border: 3px solid var(--leaf-green);
    color: var(--leaf-green-dark);
    display: flex; flex-direction: column; align-items: center; justify-content: center;
    font-weight: 700; font-size: 17px; line-height: 1.15; text-align: center;
    z-index: 2;
  }
  .ingredient-badge .count { font-size: 46px; line-height: 1; }
  .green-wave { position: absolute; left: 0; top: 560px; }
  .info {
    position: absolute;
    left: 60px; right: 60px; top: 720px;
    text-align: center;
    color: var(--paper);
  }
  .info-title {
    font-weight: 700;
    font-size: 34px;
    letter-spacing: 0.5px;
    margin-bottom: 18px;
  }
  .info-text {
    font-weight: 500;
    font-size: 22px;
    line-height: 1.4;
  }
</style>
</head>
<body>
  <main class="label">
    <div class="brand"><span>VELORAN</span><span class="brand-dot"></span></div>
    <h1 class="tagline">Wach am Morgen</h1>
    <svg class="tagline-swoosh" width="500" height="30" viewBox="0 0 500 30">
      <path d="M0 22 Q250 2 500 14" fill="none" stroke="var(--brand-blue)" stroke-width="2.5"/>
    </svg>
    <div class="fruit-illustration" role="img" aria-label="Illustration aus Äpfeln, Birne, Mango, Kiwi, Erdbeeren, Banane und Pfirsich"></div>
    <div class="ingredient-badge"><span>Mit <span class="count">70</span></span><span>Natürlichen</span><span>Zutaten</span></div>
    <svg class="green-wave" width="800" height="440" viewBox="0 0 800 440">
      <path d="M0 120 Q300 40 800 20 L800 440 L0 440 Z" fill="var(--leaf-green)"/>
      <path d="M0 380 Q400 390 800 290 L800 310 Q420 410 0 400 Z" fill="var(--paper)"/>
    </svg>
    <section class="info">
      <h2 class="info-title">MIKRONÄHRSTOFFKONZENTRAT</h2>
      <p class="info-text">Aus Obst, Gemüse, Kräutern und<br>pflanzlichen Ölen – ergänzt mit wertvollen<br>Vitaminen und Spurenelementen auf<br>wissenschaftlicher Basis.</p>
    </section>
  </main>
</body>
</html>
```